Poster for a online company that buys your stuff

SwapKestrel offers a website which customers can get a instant offer for stuff their looking to sell. They then Courier the items in to us and they get paid the same day it arrives
We're looking for an eye catching design which portrays our hassle free process
We'll need your help to come up with a slogan/catch phrase and our easy 1,2,3 process so customers can see the poster and instantly have a clear understanding of what we do
1. Get an instant offer on our website
2. Send your item(s) to us
3.Get paid within 24 Hours
Industry/Entity Type
It Company
Look and feel
Each slider illustrates characteristics of the customer's brand and the style your logo design should communicate.

```html
<!DOCTYPE html>
<html lang="en">
<head>
<meta charset="utf-8">
<title>SwapKestrel – How it works</title>
<link href="https://fonts.googleapis.com/css2?family=Roboto:wght@500;700;900&display=swap" rel="stylesheet">
<style>
  :root{
    --stage:#200e10;
    --green:#8cc63f;
    --green-mid:#79b52c;
    --green-deep:#4f8f12;
    --ink:#1a1a1a;
    --heading-dark:#353535;
    --white:#ffffff;
    --mascot-a:#8cc63f;
    --mascot-b:#f39a1e;
  }
  *{box-sizing:border-box;margin:0;padding:0}
  html,body{width:1200px;height:1200px;overflow:hidden;background:var(--stage)}
  body{position:relative;font-family:"Roboto",Arial,sans-serif}
  .poster{position:absolute;left:140px;width:921px;height:481px;background:var(--green);overflow:hidden}
  .poster--dark-icons{top:126px}
  .poster--light-icons{top:673px}
  .poster__shape{position:absolute;inset:0}
  .heading{position:absolute;left:54px;top:24px;font-weight:900;font-size:53px;letter-spacing:1px;line-height:1;white-space:nowrap}
  .heading__light{color:var(--white);border-bottom:3px solid var(--white);padding-bottom:2px}
  .heading__dark{color:var(--heading-dark);border-bottom:3px solid var(--heading-dark);padding-bottom:2px}
  .step-pill{position:absolute;top:131px;width:104px;height:34px;margin-left:-52px;background:var(--white);border-radius:12px;
    font-weight:700;font-size:18px;color:var(--ink);display:flex;align-items:center;justify-content:center}
  .step-caption{position:absolute;top:350px;width:162px;height:54px;background:var(--white);
    box-shadow:2px 2px 3px rgba(0,0,0,.18);font-weight:500;font-size:16px;line-height:20px;color:var(--ink);
    display:flex;align-items:center;justify-content:center;text-align:center}
  .mascot{position:absolute;left:616px;top:64px;width:268px;height:272px;border-radius:40px;
    background:linear-gradient(135deg,var(--mascot-a) 0%,#b9d98a 50%,var(--mascot-b) 100%)}
  .brand-name{position:absolute;left:584px;top:346px;width:320px;text-align:center;font-weight:900;font-size:54px;
    letter-spacing:-2px;color:var(--heading-dark);line-height:1;white-space:nowrap}
</style>
</head>
<body>

<section class="poster poster--dark-icons">
  <svg class="poster__shape" viewBox="0 0 921 481" width="921" height="481">
    <path d="M628 0 Q510 240 628 481 L921 481 L921 0 Z" fill="var(--green-mid)"/>
    <path d="M610 0 Q530 240 610 481 L921 481 L921 0 Z" fill="var(--green-deep)" opacity=".6"/>
    <path d="M610 0 Q550 240 610 481 L921 481 L921 0 Z" fill="var(--white)"/>
    <rect x="916" y="86" width="5" height="292" fill="var(--green-mid)"/>
    <g fill="var(--white)">
      <path d="M170 142 h10 v-6 l10 10 -10 10 v-6 h-10z"/>
      <path d="M348 142 h10 v-6 l10 10 -10 10 v-6 h-10z"/>
    </g>
    <g fill="var(--green)" stroke="var(--white)" stroke-width="5">
      <circle cx="91" cy="258" r="70"/><circle cx="265" cy="258" r="70"/><circle cx="438" cy="258" r="70"/>
    </g>
    <g fill="var(--ink)">
      <circle cx="67" cy="222" r="9"/><path d="M58 234 h18 l10 14 h14 v6 h-20 l-6 -8 v12 h10 l8 24 h-8 l-6 -18 h-18z"/>
      <rect x="60" y="286" width="4" height="12"/><rect x="84" y="260" width="52" height="6"/><rect x="108" y="266" width="22" height="34"/>
      <path d="M108 258 l10 -20 h3 l-10 20z"/>
      <path d="M228 226 h12 l18 52 h40 l10 -28 h4 l-12 34 h-46z"/>
      <circle cx="252" cy="296" r="6"/><circle cx="286" cy="296" r="6"/>
      <circle cx="289" cy="240" r="18" stroke="var(--green)" stroke-width="3"/>
      <circle cx="411" cy="222" r="9"/><path d="M402 234 h16 l10 14 h14 v6 h-22 l-4 -6 v14 h10 l6 22 h-8 l-4 -16 h-18z"/>
      <rect x="398" y="240" width="4" height="56"/><rect x="430" y="260" width="54" height="6"/><rect x="456" y="266" width="22" height="34"/>
      <path d="M466 258 l8 -26 h3 l-8 26z"/>
      <rect x="444" y="222" width="14" height="8" transform="rotate(-20 451 226)"/>
      <rect x="456" y="216" width="14" height="8"/>
      <rect x="458" y="232" width="14" height="8" transform="rotate(15 465 236)"/>
    </g>
    <path d="M281 240 l6 6 10 -12" fill="none" stroke="var(--green)" stroke-width="4"/>
  </svg>
  <h1 class="heading"><span class="heading__light">HOW IT </span><span class="heading__dark">WORKS?</span></h1>
  <div class="step-pill" style="left:91px">Step 01</div>
  <div class="step-pill" style="left:265px">Step 02</div>
  <div class="step-pill" style="left:438px">Step 03</div>
  <p class="step-caption" style="left:9px">Get an instant offer<br>on our website</p>
  <p class="step-caption" style="left:185px">Send your item(s)<br>to us</p>
  <p class="step-caption" style="left:361px">Get paid within<br>24 Hours</p>
  <div class="mascot" role="img" aria-label="Space for the brand mascot illustration"></div>
  <p class="brand-name">SwapKestrel</p>
</section>

<section class="poster poster--light-icons">
  <svg class="poster__shape" viewBox="0 0 921 481" width="921" height="481">
    <path d="M628 0 Q510 240 628 481 L921 481 L921 0 Z" fill="var(--green-mid)"/>
    <path d="M610 0 Q530 240 610 481 L921 481 L921 0 Z" fill="var(--green-deep)" opacity=".6"/>
    <path d="M610 0 Q550 240 610 481 L921 481 L921 0 Z" fill="var(--white)"/>
    <rect x="916" y="86" width="5" height="292" fill="var(--green-mid)"/>
    <g fill="var(--white)">
      <path d="M170 142 h10 v-6 l10 10 -10 10 v-6 h-10z"/>
      <path d="M348 142 h10 v-6 l10 10 -10 10 v-6 h-10z"/>
    </g>
    <g fill="var(--green)" stroke="var(--white)" stroke-width="5">
      <circle cx="91" cy="258" r="70"/><circle cx="265" cy="258" r="70"/><circle cx="438" cy="258" r="70"/>
    </g>
    <g fill="var(--white)">
      <path d="M52 248 h56 v38 h-56z M57 253 v28 h46 v-28z" fill-rule="evenodd"/>
      <path d="M42 290 h76 l-6 6 h-64z"/>
      <rect x="96" y="228" width="12" height="12"/><rect x="110" y="220" width="14" height="14"/>
      <rect x="86" y="242" width="8" height="8"/><rect x="98" y="244" width="10" height="10"/>
      <rect x="76" y="256" width="8" height="8"/><rect x="88" y="258" width="6" height="6"/>
      <rect x="68" y="266" width="8" height="8"/><rect x="110" y="238" width="8" height="8"/>
      <path d="M228 226 h12 l18 52 h40 l10 -28 h4 l-12 34 h-46z"/>
      <circle cx="252" cy="296" r="6"/><circle cx="286" cy="296" r="6"/>
      <circle cx="289" cy="240" r="18" stroke="var(--green)" stroke-width="3"/>
      <circle cx="411" cy="222" r="9"/><path d="M402 234 h16 l10 14 h14 v6 h-22 l-4 -6 v14 h10 l6 22 h-8 l-4 -16 h-18z"/>
      <rect x="398" y="240" width="4" height="56"/><rect x="430" y="260" width="54" height="6"/><rect x="456" y="266" width="22" height="34"/>
      <path d="M466 258 l8 -26 h3 l-8 26z"/>
      <rect x="444" y="222" width="14" height="8" transform="rotate(-20 451 226)"/>
      <rect x="456" y="216" width="14" height="8"/>
      <rect x="458" y="232" width="14" height="8" transform="rotate(15 465 236)"/>
    </g>
    <path d="M281 240 l6 6 10 -12" fill="none" stroke="var(--green)" stroke-width="4"/>
  </svg>
  <h1 class="heading"><span class="heading__light">HOW IT </span><span class="heading__dark">WORKS?</span></h1>
  <div class="step-pill" style="left:91px">Step 01</div>
  <div class="step-pill" style="left:265px">Step 02</div>
  <div class="step-pill" style="left:438px">Step 03</div>
  <p class="step-caption" style="left:9px">Get an instant offer<br>on our website</p>
  <p class="step-caption" style="left:185px">Send your item(s)<br>to us</p>
  <p class="step-caption" style="left:361px">Get paid within<br>24 Hours</p>
  <div class="mascot" role="img" aria-label="Space for the brand mascot illustration"></div>
  <p class="brand-name">SwapKestrel</p>
</section>

</body>
</html>
```